Electrical company business card design.

Hi, were an electrical company in Auckland New Zealand called Quarneth Ltd. We focus mainly on high end residential and commercial so the card would be targeted towards that.
The card will be for myself, i am the director of the company.
Name: Derek Olstow
Position: Director/electrician
Phone: 021 387 9415
Email: derek@quarneth.co.nz
Location: Auckland
As for colors the the blue color in the logo is preferred, i also don't mind a black background option.
Target Market(s)
High end residential and commercial
Industry/Entity Type
Electrician
Contact Information for Business Card
Name: Derek Olstow Position: Director/Electrician Phone: 021 387 9415, Email: derek@quarneth.co.nz, Location: Auckland

```html
<!DOCTYPE html>
<html lang="en">
<head>
<meta charset="utf-8">
<title>Quarneth Ltd — Business Card</title>
<link href="https://fonts.googleapis.com/css2?family=Arimo:wght@400;700&display=swap" rel="stylesheet">
<style>
  :root {
    --stage: #3d3d3d;
    --paper: #ffffff;
    --brand-blue: #1456b0;
    --brand-blue-light: #0a86cf;
    --brand-cyan: #35d0ec;
    --ink-grey: #555a5e;
    --soft-grey: #8a8f93;
    --block-grey: #53575a;
    --rule: #c9cccf;
  }
  * { box-sizing: border-box; margin: 0; padding: 0; }
  html, body { width: 1200px; height: 803px; overflow: hidden; }
  body {
    background: var(--stage);
    font-family: "Arimo", Arial, sans-serif;
    display: flex;
    align-items: center;
    justify-content: center;
    gap: 60px;
  }
  .card {
    position: relative;
    width: 520px;
    height: 300px;
    border-radius: 20px;
    overflow: hidden;
    box-shadow: 0 14px 30px rgba(0,0,0,0.35);
  }

  /* Front */
  .card--front { background: var(--paper); }
  .front__brand {
    position: absolute;
    left: 44px;
    top: 92px;
    width: 210px;
  }
  .brand-name {
    font-weight: 700;
    letter-spacing: 1px;
    white-space: nowrap;
  }
  .front__brand .brand-name {
    font-size: 30px;
    color: var(--ink-grey);
  }
  .front__brand .tagline {
    margin-top: 4px;
    font-size: 9.5px;
    font-weight: 700;
    letter-spacing: 1.6px;
    color: var(--ink-grey);
    white-space: nowrap;
  }
  .front__divider {
    position: absolute;
    left: 262px;
    top: 70px;
    width: 1px;
    height: 110px;
    background: linear-gradient(to bottom, transparent, var(--rule), transparent);
  }
  .front__contact {
    position: absolute;
    left: 284px;
    top: 72px;
  }
  .person-name {
    font-size: 21px;
    font-weight: 700;
    color: var(--brand-blue);
  }
  .person-role {
    font-size: 11px;
    color: var(--soft-grey);
    margin-top: 2px;
  }
  .person-city {
    font-size: 12px;
    color: var(--ink-grey);
    margin-top: 22px;
  }
  .person-phone {
    display: flex;
    align-items: center;
    gap: 7px;
    font-size: 13px;
    color: var(--ink-grey);
    margin-top: 12px;
  }
  .person-phone svg { width: 11px; height: 11px; fill: var(--brand-blue); }
  .front__band {
    position: absolute;
    left: 0;
    bottom: 40px;
    width: 456px;
    height: 34px;
    background: linear-gradient(90deg, var(--brand-blue) 0%, var(--brand-blue-light) 55%, var(--brand-blue) 100%);
    display: flex;
    align-items: center;
    justify-content: center;
  }
  .front__band .web {
    color: var(--paper);
    font-size: 12px;
    letter-spacing: 3px;
  }
  .front__marker {
    position: absolute;
    left: 462px;
    bottom: 49px;
    width: 16px;
    height: 16px;
    border-radius: 50%;
    background: var(--brand-blue);
  }
  .front__block {
    position: absolute;
    right: 0;
    bottom: 74px;
    width: 36px;
    height: 52px;
    background: var(--block-grey);
  }

  /* Back */
  .card--back {
    background: radial-gradient(ellipse at 40% 45%, #0a8fd6 0%, #0b6cc2 45%, #1547a0 100%);
    display: flex;
    flex-direction: column;
    align-items: center;
    justify-content: center;
  }
  .card--back .brand-name {
    font-size: 52px;
    color: var(--brand-cyan);
    letter-spacing: 3px;
  }
  .card--back .tagline {
    margin-top: 6px;
    font-size: 14px;
    font-weight: 700;
    letter-spacing: 3px;
    color: var(--brand-cyan);
    white-space: nowrap;
  }
</style>
</head>
<body>
  <section class="card card--front" aria-label="Business card front">
    <div class="front__brand">
      <div class="brand-name">QUARNETH</div>
      <div class="tagline">CURRENT WITH CRAFT</div>
    </div>
    <div class="front__divider"></div>
    <div class="front__contact">
      <div class="person-name">Derek Olstow</div>
      <div class="person-role">Director/electrician</div>
      <div class="person-city">Auckland</div>
      <div class="person-phone">
        <svg viewBox="0 0 24 24" aria-hidden="true"><path d="M6.6 10.8a15.1 15.1 0 0 0 6.6 6.6l2.2-2.2a1 1 0 0 1 1-.25 11.4 11.4 0 0 0 3.6.57 1 1 0 0 1 1 1V20a1 1 0 0 1-1 1A17 17 0 0 1 3 4a1 1 0 0 1 1-1h3.5a1 1 0 0 1 1 1c0 1.25.2 2.45.57 3.57a1 1 0 0 1-.25 1z"/></svg>
        <span>021 387 9415</span>
      </div>
    </div>
    <div class="front__band"><span class="web">www.QUARNETH.com</span></div>
    <div class="front__marker"></div>
    <div class="front__block"></div>
  </section>

  <section class="card card--back" aria-label="Business card back">
    <div class="brand-name">QUARNETH</div>
    <div class="tagline">CURRENT WITH CRAFT</div>
  </section>
</body>
</html>
```